Electrical Wholesaler Needs a New Website

Looking for a new website to be built for an electrical wholesaler based in Birmingham(England). Our logo is based on two Lions with a shield, so ideally the site should be deigned around that.

Looking for something that shows off our logo and incorporates what we are trying to do, preferably to have a colour scheme that is green and black if possible.

Target Market(s)

I'm looking for a professional website for my company that doesn't just look like amother WordPress template that I could build myself.

Industry/Entity Type

Electrical

Font styles to use
Sans Serif

Colors
9bcb3c
cadf82

Requirements
Must have
• Website with 4-5 pages, home page, about us, suppliers list, catalogue download and contact us. Search for UK electrical wholesalers to give you an idea of what I mean.

```html
<!DOCTYPE html>
<html lang="en">
<head>
<meta charset="utf-8">
<title>Volta Electrical Wholesalers</title>
<link href="https://fonts.googleapis.com/css2?family=Roboto+Condensed:wght@400;700&family=Open+Sans:wght@400;600;700&display=swap" rel="stylesheet">
<style>
:root{
  --green:#8dc63f;
  --green-bright:#9bcb3c;
  --green-light:#cadf82;
  --green-lime:#a6e22e;
  --dark:#333333;
  --nav:#3b3b3b;
  --text:#444444;
  --muted:#888888;
  --line:#dddddd;
  --page:#efefef;
  --white:#ffffff;
  --sale:#f0506e;
}
*{box-sizing:border-box;margin:0;padding:0}
html,body{width:857px;height:1200px;overflow:hidden}
body{background:var(--page);font-family:"Open Sans",Arial,sans-serif;color:var(--text);position:relative}
.site{position:absolute;left:86px;top:22px;width:685px;height:1030px;background:var(--white);box-shadow:0 0 4px rgba(0,0,0,.08);overflow:hidden}
.abs{position:absolute}

/* header */
.brand{left:10px;top:10px;width:90px;text-align:center}
.brand-mark{display:inline-block;width:22px;height:22px;border-radius:50%;background:var(--green);vertical-align:middle}
.brand-name{font-family:"Roboto Condensed",sans-serif;font-weight:700;font-size:36px;line-height:40px;color:var(--dark);display:block;margin-top:4px}
.brand-sub{font-family:"Roboto Condensed",sans-serif;font-size:7px;color:var(--green);letter-spacing:.2px;display:block}
.toplinks{left:432px;top:11px;display:flex;gap:22px;font-family:"Roboto Condensed",sans-serif;font-size:10px;color:var(--dark)}
.toplinks span{display:flex;align-items:center;gap:5px}
.btn-green{background:var(--green);color:var(--white);font-family:"Roboto Condensed",sans-serif;font-size:12px;display:flex;align-items:center;justify-content:center;gap:4px;height:27px;letter-spacing:.3px}
.create{left:297px;top:51px;width:123px}
.login{left:421px;top:51px;width:63px}
.cart{left:491px;top:46px;width:184px;height:39px;background:var(--dark);color:var(--white);display:flex;align-items:center;padding-left:12px}
.cart b{font-size:16px;margin-right:4px}
.cart small{font-size:10px}
.cart svg{position:absolute;right:10px;top:16px}

.nav{left:0;top:96px;width:685px;height:29px;background:var(--nav);display:flex;font-family:"Roboto Condensed",sans-serif;font-size:10.5px;color:var(--white)}
.nav a{display:flex;align-items:center;padding:0 13px;color:inherit;text-decoration:none}
.nav a.active{background:var(--green);width:50px;justify-content:center;padding:0}

/* sidebar */
.cats{left:3px;top:133px;width:182px;border:1px solid var(--line)}
.cats h2{height:25px;background:linear-gradient(#a8d65a,var(--green));color:#223;font-family:"Roboto Condensed",sans-serif;font-size:13px;font-weight:700;padding-left:12px;display:flex;align-items:center}
.cats li{list-style:none;height:22px;border-top:1px solid var(--line);font-family:"Roboto Condensed",sans-serif;font-size:9.5px;color:var(--dark);padding-left:13px;display:flex;align-items:center;position:relative}
.cats li:first-child{background:#f2f7e6}
.cats li:first-child:after{content:"";position:absolute;right:8px;border-left:4px solid var(--green);border-top:4px solid transparent;border-bottom:4px solid transparent}

.promo{left:3px;top:446px;width:181px;height:254px;background:var(--green-lime)}
.promo-photo{position:absolute;left:0;top:10px;width:181px;height:150px;background:linear-gradient(135deg,#d9d9d9,#8a5a3a 55%,#2b2b2b)}
.promo h3{position:absolute;top:163px;width:100%;text-align:center;font-family:"Roboto Condensed",sans-serif;font-size:12px;color:var(--white);font-weight:700}
.promo p{position:absolute;top:180px;left:7px;right:7px;font-size:7.5px;line-height:11px;color:#223;text-align:center}
.promo .shop{position:absolute;left:45px;top:215px;width:91px;height:33px;background:#111;color:var(--white);font-size:12px;display:flex;align-items:center;justify-content:center}

.ask{left:6px;top:723px;width:172px;height:155px;border:1px solid #ccc;background:linear-gradient(#f6f6f6,#e2e2e2);overflow:hidden}
.ask-band{position:absolute;left:0;top:0;width:100%;height:46px;background:var(--green-bright)}
.ask h3{position:absolute;left:10px;top:10px;font-size:20px;color:var(--white);font-weight:600}
.ask-photo{position:absolute;right:0;top:40px;width:100px;height:115px;background:linear-gradient(160deg,#cfcfcf,#8b7766 60%,#333)}
.ask a{position:absolute;left:10px;top:56px;font-size:12px;color:#1a6fb0;text-decoration:underline}
.ask small{position:absolute;left:10px;top:73px;font-size:8px;color:#1a6fb0}

.ship{left:7px;top:903px;width:170px;height:96px;background:var(--green-bright);color:var(--white);text-align:center;padding-top:14px}
.ship b{display:block;font-size:17px;font-weight:700;line-height:20px}
.ship strong{display:block;font-size:11px;font-weight:700}
.ship small{display:block;font-size:7px;line-height:11px;margin-top:3px}

/* banner */
.banner{left:194px;top:134px;width:484px;height:231px;border:1px solid #e4e4e4;background:#fafafa;overflow:hidden}
.banner-art{position:absolute;inset:0;background:linear-gradient(120deg,#fafafa 0%,#fafafa 45%,#e9f3d6 62%,#2f7a2a 100%)}
.banner-cables{position:absolute;left:10px;top:75px;width:330px;height:150px;border-radius:50% 50% 10px 10px;background:radial-gradient(circle at 50% 60%,#f0a040,#c83a1e 50%,#2b2b2b 80%,transparent 81%)}
.banner h1{position:absolute;left:15px;top:8px;font-family:"Roboto Condensed",sans-serif;font-weight:400;font-size:21px;color:#333}
.banner h2{position:absolute;left:15px;top:30px;font-family:"Roboto Condensed",sans-serif;font-weight:700;font-size:32px;letter-spacing:1.5px;color:var(--green)}

.search{left:194px;top:375px;width:484px;height:46px;border:1px solid #e4e4e4;border-radius:6px;background:#f8f8f8}
.search-field{position:absolute;left:13px;top:9px;width:403px;height:28px;background:var(--white);border:1px solid #ddd}
.search-field svg{position:absolute;left:7px;top:6px}
.search-field i{position:absolute;left:28px;top:0;bottom:0;border-left:1px solid #ddd}
.search-btn{position:absolute;left:416px;top:9px;width:60px;height:28px;background:#444;color:var(--white);font-size:11px;display:flex;align-items:center;justify-content:center}

/* tabs */
.tabs{left:195px;top:446px;width:474px;height:28px;border-bottom:1px solid var(--line)}
.tab-on{position:absolute;left:0;top:0;width:116px;height:25px;background:var(--green);color:var(--white);font-size:12px;display:flex;align-items:center;justify-content:center}
.tab-on:after{content:"";position:absolute;bottom:-6px;left:54px;border-top:6px solid var(--green);border-left:6px solid transparent;border-right:6px solid transparent}
.tab{position:absolute;top:5px;font-size:12px;color:#222}
.sep{position:absolute;top:8px;width:1px;height:12px;background:#aaa}
.select{position:absolute;left:340px;top:2px;width:131px;height:19px;border:1px solid #ccc;font-size:8px;color:#555;padding-left:7px;display:flex;align-items:center}
.select:after{content:"";position:absolute;right:7px;top:7px;border-top:5px solid #aaa;border-left:4px solid transparent;border-right:4px solid transparent}

.card{width:147px;height:178px;border:1px solid #ddd;background:var(--white)}
.card-img{position:absolute;left:30px;top:8px;width:86px;height:82px;border-radius:8px}
.card h4{position:absolute;left:14px;top:92px;width:120px;height:25px;background:#f2f2f2;font-size:8px;font-weight:600;color:#222;padding-left:6px;display:flex;align-items:center}
.card p{position:absolute;left:14px;top:121px;width:120px;font-size:8px;line-height:12px;color:var(--muted)}
.card .price{position:absolute;left:14px;top:152px;font-family:"Roboto Condensed",sans-serif;font-size:12px;color:var(--green)}
.card .buy{position:absolute;left:75px;top:150px;width:52px;height:16px;background:#3a3a3a;color:var(--white);font-size:8.5px;font-weight:600;display:flex;align-items:center;justify-content:center}
.sale{position:absolute;right:4px;top:40px;width:27px;height:58px;background:var(--sale);color:var(--white);font-size:9px;font-weight:700;writing-mode:vertical-rl;display:flex;align-items:center;justify-content:center;clip-path:polygon(0 0,100% 0,100% 100%,0 86%)}
.tone-dark{background:linear-gradient(#3a3a3a,#111)}
.tone-steel{background:linear-gradient(90deg,#777,#eee 45%,#888)}
.tone-blue{background:radial-gradient(circle,#3c5ad0,#1d2f80 65%,#cfd4e6)}
.tone-plate{background:linear-gradient(#fafafa,#dcdcdc);border:1px solid #ccc}

.viewall{left:195px;top:894px;width:474px;height:1px;background:var(--line)}
.viewall span{position:absolute;left:217px;top:-7px;width:50px;height:13px;background:#3a3a3a;color:var(--white);font-size:7.5px;display:flex;align-items:center;justify-content:center}

.deals{left:198px;top:918px;width:472px;height:96px;border:1px solid #e4e4e4;background:linear-gradient(#eee,#fafafa 40%)}
.deals h3{position:absolute;left:0;width:100%;top:8px;text-align:center;font-family:"Roboto Condensed",sans-serif;font-size:14px;color:var(--green);font-weight:700}
.deals h3:before,.deals h3:after{content:"";position:absolute;top:8px;width:7px;height:7px;border-radius:50%;background:#bbb}
.deals h3:before{left:180px}.deals h3:after{right:168px}
.deal-row{position:absolute;left:8px;right:8px;top:40px;height:50px;display:flex;justify-content:space-around;align-items:center}
.deal{font-size:17px;font-weight:700;color:#333;display:flex;align-items:center;gap:5px}
.deal i{display:inline-block;width:14px;height:14px;border-radius:50%;background:#c41e2a}

/* footer */
.foot{position:absolute;top:1070px;left:86px;width:685px;height:120px}
.foot-brand{left:8px;top:4px;width:92px;text-align:center}
.foot-brand .brand-sub{color:#333}
.copy{left:24px;top:106px;font-size:7.5px;color:#555}
.foot h5{font-family:"Roboto Condensed",sans-serif;font-size:13px;font-weight:400;color:#444}
.vr{width:1px;background:#ddd;top:0;height:120px}
.news-in{left:128px;top:30px;width:167px;height:20px;border:1px solid #ccc;border-radius:10px;background:#f4f4f4}
.news-in i{position:absolute;right:4px;top:3px;width:16px;height:12px;background:var(--green)}
.social{left:131px;top:92px;display:flex;gap:8px}
.social span{width:21px;height:21px;border-radius:50%;background:#1f6fb0;border:2px solid #ddd}
.links{font-family:"Roboto Condensed",sans-serif;font-size:9.5px;color:#333;line-height:19.2px;list-style:none}
.links li:before{content:"";display:inline-block;margin-right:7px;border-left:3px solid var(--green);border-top:3px solid transparent;border-bottom:3px solid transparent;vertical-align:middle}
.cards{left:526px;top:24px;display:flex;gap:4px}
.cards span{width:30px;height:18px;border:1px solid #ccc;background:#fff;font-size:6.5px;font-weight:700;color:#333;display:flex;align-items:center;justify-content:center}
.secured{left:526px;top:66px;display:flex;align-items:center;gap:5px}
.seals{left:526px;top:88px;display:flex;gap:6px}
.seals span{width:32px;height:12px;border-radius:3px;background:#cfcfcf}
</style>
</head>
<body>
<div class="site">
  <div class="abs brand"><span class="brand-mark"></span><span class="brand-name">VOLTA</span><span class="brand-sub">ELECTRICAL WHOLESALERS</span></div>

  <div class="abs toplinks">
    <span><svg width="10" height="11" viewBox="0 0 10 11"><circle cx="5" cy="3" r="2.5" fill="#333"/><rect x="1" y="6" width="8" height="5" rx="2" fill="#333"/></svg>My Account</span>
    <span><svg width="14" height="11" viewBox="0 0 14 11"><path d="M0 1h3l2 6h7l2-5H4" fill="none" stroke="#333" stroke-width="1.5"/><circle cx="6" cy="9.5" r="1.3" fill="#333"/><circle cx="11" cy="9.5" r="1.3" fill="#333"/></svg>Shopping Cart</span>
    <span><svg width="12" height="10" viewBox="0 0 12 10"><path d="M1 5l3 3 7-7" fill="none" stroke="#222" stroke-width="2"/></svg>Checkout</span>
  </div>
  <div class="abs btn-green create"><svg width="8" height="8" viewBox="0 0 8 8"><rect x=".5" y=".5" width="7" height="7" fill="none" stroke="#fff"/><path d="M4 2v4M2 4h4" stroke="#fff"/></svg>Create an account</div>
  <div class="abs btn-green login"><svg width="8" height="10" viewBox="0 0 8 10"><path d="M2 4V3a2 2 0 0 1 4 0v1" fill="none" stroke="#fff" stroke-width="1.2"/><rect x="1" y="4" width="6" height="5" fill="#fff"/></svg>Login</div>
  <div class="abs cart"><b>CART:</b><small>0 item(s) <b style="font-size:10px">$0.00</b></small>
    <svg width="9" height="6" viewBox="0 0 9 6"><path d="M1 1l3.5 3.5L8 1" fill="none" stroke="#fff" stroke-width="1.5"/></svg></div>

  <nav class="abs nav"><a class="active">Home</a><a>About Us</a><a>Products Categories</a><a>Delivery</a><a style="padding-left:21px">Manufacturers</a><a>Contact Us</a></nav>

  <aside class="abs cats">
    <h2>Catgories</h2>
    <ul>
      <li>Industrial Automation</li><li>Inverter Drives</li><li>Industrial Control</li><li>Distributuon &amp; Switchgear</li><li>Sensing &amp; Safety</li><li>Enclosures &amp; Panel Products</li><li>Sounding &amp; Signalling</li><li>Cable &amp; Cable Management</li><li>Lighting</li><li>Wiring Accessories</li><li>Heating &amp; Ventilation</li><li>Tools &amp; JEnitorial</li>
    </ul>
  </aside>

  <div class="abs promo">
    <div class="promo-photo" role="img" aria-label="Photo of bundled electrical cables with copper cores"></div>
    <h3>NULLA UT ERAT NULLA</h3>
    <p>Suspendisse potenti. Ut purus eros, tristi-que in porta quis, lobortis sed lacus...</p>
    <div class="shop">Shop now!</div>
  </div>

  <div class="abs ask">
    <div class="ask-band"></div>
    <div class="ask-photo" role="img" aria-label="Photo of a thoughtful man"></div>
    <h3>Any questions?</h3>
    <a>Click here</a><small>to contact us</small>
  </div>

  <div class="abs ship"><b>FREE SHIPPING</b><strong>ON ORDERS OVER $99</strong><small>THIS OFFER IS VALID ON ALL<br>OUR STORE ITEMS.</small></div>

  <section class="abs banner">
    <div class="banner-art" role="img" aria-label="Illustration of coloured electrical cables beside a green heraldic lion"></div>
    <div class="banner-cables"></div>
    <h1>World’s Renowned and Branded</h1>
    <h2>Electrical Products</h2>
  </section>

  <div class="abs search">
    <div class="search-field"><svg width="14" height="14" viewBox="0 0 14 14"><circle cx="6" cy="6" r="4.5" fill="none" stroke="#999" stroke-width="1.8"/><path d="M9.5 9.5L13 13" stroke="#999" stroke-width="2"/></svg><i></i></div>
    <div class="search-btn">Search</div>
  </div>

  <div class="abs tabs">
    <div class="tab-on">Recommended</div>
    <span class="sep" style="left:126px"></span><span class="tab" style="left:141px">New Products</span>
    <span class="sep" style="left:229px"></span><span class="tab" style="left:241px">Best Sellers</span>
    <div class="select">Select Product</div>
  </div>

  <article class="abs card" style="left:196px;top:499px"><div class="card-img tone-dark" style="top:30px;height:40px;border-radius:2px" role="img" aria-label="Product photo of an AV receiver"></div><h4>Tekra TK760</h4><p>Laoreet dolore magnaorem ipsum dolor ser adipiscin...</p><span class="price">$39.99</span><span class="buy">Buy Now</span></article>
  <article class="abs card" style="left:359px;top:499px"><div class="card-img tone-steel" style="left:42px;width:60px" role="img" aria-label="Product photo of a steel kettle"></div><span class="sale">SALE</span><h4>Tekra TK760</h4><p>Laoreet dolore magnaorem ipsum dolor ser adipiscin...</p><span class="price">$39.99</span><span class="buy">Buy Now</span></article>
  <article class="abs card" style="left:523px;top:499px"><div class="card-img tone-blue" role="img" aria-label="Product photo of a blue vacuum cleaner"></div><h4>Tekra TK760</h4><p>Laoreet dolore magnaorem ipsum dolor ser adipiscin...</p><span class="price">$39.99</span><span class="buy">Buy Now</span></article>
  <article class="abs card" style="left:196px;top:691px;height:175px"><div class="card-img tone-steel" style="left:42px;width:60px" role="img" aria-label="Product photo of a steel kettle"></div><h4>Tekra TK760</h4><p>Laoreet dolore magnaorem ipsum dolor ser adipiscin...</p><span class="price">$39.99</span><span class="buy">Buy Now</span></article>
  <article class="abs card" style="left:359px;top:691px;height:175px"><div class="card-img tone-blue" role="img" aria-label="Product photo of a blue vacuum cleaner"></div><h4>Tekra TK760</h4><p>Laoreet dolore magnaorem ipsum dolor ser adipiscin...</p><span class="price">$39.99</span><span class="buy">Buy Now</span></article>
  <article class="abs card" style="left:523px;top:691px;height:175px"><div class="card-img tone-plate" style="left:22px;width:100px;top:20px;height:60px;border-radius:3px" role="img" aria-label="Product photo of a double wall socket"></div><h4>Tekra TK760</h4><p>Laoreet dolore magnaorem ipsum dolor ser adipiscin...</p><span class="price">$39.99</span><span class="buy">Buy Now</span></article>

  <div class="abs viewall"><span>VIEW ALL</span></div>

  <section class="abs deals">
    <h3>DEALS IN</h3>
    <div class="deal-row">
      <span class="deal"><i></i>Halden</span>
      <span class="deal">Marketon</span>
      <span class="deal" style="color:#1f5fb0">Orbis</span>
      <span class="deal" style="color:#e8792a">Lumeo</span>
      <span class="deal" style="color:#1f5fb0">Brightway</span>
    </div>
  </section>
</div>

<footer class="foot">
  <div class="abs foot-brand"><span class="brand-mark" style="background:#333"></span><span class="brand-name">VOLTA</span><span class="brand-sub">ELECTRICAL WHOLESALERS</span></div>
  <div class="abs copy">© Copyright, 2014</div>
  <div class="abs vr" style="left:118px"></div>
  <h5 class="abs" style="left:133px;top:0">Newsletter Signup</h5>
  <div class="abs news-in"><i></i></div>
  <h5 class="abs" style="left:132px;top:68px">Get Connected</h5>
  <div class="abs social" aria-label="Social links"><span></span><span></span><span></span><span style="background:#e8792a"></span><span style="background:#d33"></span></div>
  <div class="abs vr" style="left:306px"></div>
  <h5 class="abs" style="left:315px;top:0">Featured Links</h5>
  <ul class="abs links" style="left:315px;top:18px"><li>Delivery Information</li><li>Terms &amp; Conditions</li><li>Privacy Policy</li><li>Returns Policy</li><li>Help</li></ul>
  <ul class="abs links" style="left:428px;top:18px"><li>About Us</li><li>Manufacturers</li><li>Products</li><li>Delivery</li><li>Contacts</li></ul>
  <div class="abs vr" style="left:513px"></div>
  <h5 class="abs" style="left:527px;top:0">We Accept</h5>
  <div class="abs cards"><span>Carda</span><span>Duocard</span><span>Paylink</span><span>Netpay</span></div>
  <div class="abs secured"><h5>Secured by</h5><svg width="10" height="13" viewBox="0 0 10 13"><path d="M2.5 6V4a2.5 2.5 0 0 1 5 0v2" fill="none" stroke="#e0a020" stroke-width="1.6"/><rect x="1" y="6" width="8" height="7" rx="1" fill="#e0a020"/></svg></div>
  <div class="abs seals"><span></span><span></span><span></span><span></span></div>
</footer>
</body>
</html>
```